Long Term Contract - Wordpress Designers Wanted!

We are rapidly growing start-up web development company, focused on website development geared towards the insurance industry.

To increase our impact, we’ve decided to add a freelance designer to the team to assist in graphical elements and webdesign for our clients and template development.

This is to screen for a LONG TERM relationship where we will work together to design and develop sites for insurance agents. We are seeking a talented web designer with experience in WordPress and WordPress theme development to work his/her magic on our new websites.

To win this contest, please create an example website design for an individual insurance agent that sells auto and home insurance. The website will essentially be a "business card" for the agent and will generate trust, show experience, and most importantly create a call to action for the person to call or get a quote.

An example is here:

http://tallowgrid.com/heron/

As part of the deliverable, we will want you to integrate these templates as child themes under Quillix "Marlow" template framework - which we can provide you of course. All forms should be done in velvet forms.

Target Market(s)

Audience: consumers shopping for insurance agent

Industry/Entity Type

Insurance

Requirements
Must have
• Pages:
-home
-products
-about
-news/blog
-Contact us

On home page the following elements should be included:
-contact us form
-agent contact information
-blog entries
-testimonial
-agency overview
Should not have
• flash

```html
<!DOCTYPE html>
<html lang="en">
<head>
<meta charset="utf-8">
<title>Company Name – Auto &amp; Home Insurance Agent</title>
<link rel="stylesheet" href="https://fonts.googleapis.com/css2?family=Arimo:wght@400;700&family=Gelasio&family=Open+Sans:wght@400;600&family=Yanone+Kaffeesatz:wght@600&display=swap">
<style>
:root{
  --red:#e30613;
  --text:#444;
  --muted:#777;
  --light:#f4f4f4;
  --band:#e9e9e9;
  --border:#d6d6d6;
  --dark:#2e2e2e;
  --footer-text:#cfcfcf;
}
*{margin:0;padding:0;box-sizing:border-box}
html,body{width:857px;height:1200px;overflow:hidden;background:#fff}
body{font-family:"Arimo",Arial,sans-serif;color:var(--text)}
.page{position:relative;width:857px;height:1200px;overflow:hidden;background:var(--light)}
.abs{position:absolute}

/* header */
.site-header{left:0;top:0;width:857px;height:78px;background:linear-gradient(#fdfdfd,#ededed);border-bottom:1px solid #ddd}
.logo{left:31px;top:24px;font-family:"Gelasio",Georgia,serif;font-size:24px;color:#333}
.main-nav a{position:absolute;top:24px;height:26px;line-height:26px;font-size:12.5px;color:#222;text-decoration:none;white-space:nowrap}
.main-nav a.active{background:linear-gradient(#bdbdbd,#9a9a9a);color:#fff;border-radius:3px;padding:0 12px}

/* hero */
.hero{left:0;top:78px;width:857px;height:326px;background:linear-gradient(#e6e6e6,#f7f7f7 30%,#f3f3f3)}
.portrait-frame{left:51px;top:94px;width:215px;height:286px;background:#fff;border:1px solid #ccc;box-shadow:0 1px 3px rgba(0,0,0,.15)}
.portrait{left:62px;top:104px;width:191px;height:265px;background:linear-gradient(160deg,#2a1a18,#7a2a1e 40%,#d8b6a2 60%,#3a3a3a)}
.hero-title{left:342px;top:97px;width:482px;font-size:17.5px;font-weight:400;color:#222;padding-bottom:6px;border-bottom:1px solid #cfcfcf;white-space:nowrap}
.hero-title span{color:var(--red)}
.hero-intro{left:342px;top:131px;width:482px;font-size:12.4px;line-height:16px;color:#444}
.benefits{left:342px;top:188px;list-style:none;font-size:13.3px}
.benefits li{height:23px;padding-left:19px;position:relative;color:#555;white-space:nowrap}
.benefits li::before{content:"";position:absolute;left:3px;top:5px;width:5px;height:5px;border-right:2px solid #555;border-bottom:2px solid #555;transform:rotate(-45deg)}
.benefits b{color:var(--red)}
.hero-rule{left:342px;top:282px;width:482px;height:1px;background:#cfcfcf}
.call-title{left:342px;top:290px;font-size:16px;font-weight:700;color:#333;white-space:nowrap}
.call-title span{color:var(--red)}
.call-sub{left:342px;top:313px;font-size:10.6px;color:#555;letter-spacing:.2px;white-space:nowrap}
.quote-form input{position:absolute;top:335px;height:22px;border:1px solid #ddd;border-radius:3px;background:#fafafa;font:10.5px "Arimo",sans-serif;color:#aaa;padding:0 8px}
.submit{left:757px;top:367px;width:66px;height:24px;background:linear-gradient(#f0232a,#c4000a);border:1px solid #a30008;border-radius:2px;color:#fff;font:14px "Arimo",sans-serif}

.band{left:0;width:857px;background:linear-gradient(#e4e4e4,#f0f0f0)}

/* overview */
.overview-bg{left:0;top:434px;width:857px;height:94px;background:#f6f6f6}
.overview-icon{left:28px;top:434px;width:26px;height:26px;border-radius:3px;background:linear-gradient(135deg,#f0b73a,#d9d9d9)}
.section-title{font-family:"Open Sans",Arial,sans-serif;font-weight:600;color:#444}
.overview h2{left:61px;top:436px;font-size:17px}
.overview p{left:29px;top:471px;width:800px;font-size:11px;line-height:16px;color:#555;letter-spacing:.2px}
.overview p a{color:var(--red);text-decoration:none}

/* products */
.products{left:0;top:558px;width:857px;height:225px;background:#f4f4f4}
.product{position:absolute;top:570px;width:164px}
.product h3{font-size:13px;font-weight:700;color:var(--red);height:20px;white-space:nowrap}
.product .thumb{width:164px;height:66px;background:#fff;border:1px solid #ddd;display:flex;align-items:center;justify-content:center}
.product .thumb span{display:block;width:60px;height:50px;border-radius:6px}
.product p{margin-top:8px;font-size:10.6px;line-height:15.9px;color:#555;text-align:justify}

/* news */
.news-bg{left:25px;top:783px;width:798px;height:154px;background:#fff;border:1px solid #ddd;border-radius:3px;box-shadow:0 1px 3px rgba(0,0,0,.1)}
.news h2{left:42px;top:794px;font-size:19px;font-family:"Open Sans",Arial,sans-serif;color:#333;font-weight:400}
.arrow{top:790px;width:23px;height:23px;border-radius:50%;background:linear-gradient(#fff,#e5e5e5);border:1px solid #ccc;display:flex;align-items:center;justify-content:center}
.news-photo{left:39px;top:830px;width:257px;height:92px;border:4px solid #f2f2f2;background:linear-gradient(90deg,#c9c2b8,#8a8078 45%,#c6ccd2 70%,#5a6068)}
.news h3{left:320px;top:826px;font-size:15px;font-weight:700;color:#444;letter-spacing:.4px}
.news p{left:320px;top:854px;width:485px;font-size:10.8px;line-height:16px;color:#555;letter-spacing:.2px}
.news .read{left:320px;top:902px;font-size:11px;font-weight:700;color:#444;letter-spacing:.5px}

/* footer */
.site-footer{left:0;top:960px;width:857px;height:240px;background:linear-gradient(#333,#272727)}
.footer-title{font-family:"Yanone Kaffeesatz","Oswald",sans-serif;font-weight:600;font-size:27px;color:#fff;top:975px;white-space:nowrap}
.footer-text{font-size:10.6px;line-height:16px;color:var(--footer-text);letter-spacing:.3px}
.btn{height:22px;width:71px;background:linear-gradient(#fff,#ddd);border-radius:2px;font-size:9.5px;color:#333;text-align:center;line-height:22px}
.social{left:658px;top:1022px;list-style:none}
.social li{height:23px;display:flex;align-items:center;font-size:11px;color:#fff;font-family:"Open Sans",Arial,sans-serif}
.social i{display:inline-block;width:13px;height:13px;margin:0 13px 0 0;border-radius:2px}
.footer-rule{left:0;top:1149px;width:857px;height:1px;background:#484848}
.copyright{left:31px;top:1173px;font-size:9.8px;color:#fff}
.footer-nav a{position:absolute;top:1171px;font-size:11px;color:#8c8c8c;text-decoration:none;white-space:nowrap}
</style>
</head>
<body>
<div class="page">

  <header class="site-header abs">
    <div class="logo abs">Company Name</div>
    <nav class="main-nav">
      <a class="active" style="left:366px">Auto Insurance</a>
      <a style="left:490px">Home Insurance</a>
      <a style="left:605px">Products</a>
      <a style="left:690px">News</a>
      <a style="left:756px">Contact Us</a>
    </nav>
  </header>

  <section class="hero abs"></section>
  <div class="portrait-frame abs"></div>
  <div class="portrait abs" role="img" aria-label="Portrait photo of the insurance agent"></div>
  <h1 class="hero-title abs">Answer your insurance questions here at <span>Insurance Company</span></h1>
  <p class="hero-intro abs">We serve New Hampshire, Massachusetts and Maine with the best in auto and home insurance advice. Get free, professional advice on how to protect your car, your house and your family, including:</p>
  <ul class="benefits abs">
    <li><b>Auto Insurance:</b> take your questions to an expert</li>
    <li><b>Home Insurance:</b> the confusion will end</li>
    <li><b>Auto &amp; Home Bundles:</b> A+ rated companies, best rates</li>
    <li><b>Renters Coverage:</b> safe haven for belongings</li>
  </ul>
  <div class="hero-rule abs"></div>
  <h2 class="call-title abs">Call Us At <span>1-555-010-2468</span> For A Free Quote</h2>
  <p class="call-sub abs">I can help you sort through your options and will review current coverage, at no cost to you.</p>
  <form class="quote-form">
    <input style="left:340px;width:137px" value="First Name">
    <input style="left:490px;width:138px" value="Phone no.">
    <input style="left:637px;width:187px" value="Email Address">
    <button class="submit abs" type="button">Submit</button>
  </form>

  <div class="band abs" style="top:404px;height:30px"></div>

  <section class="overview-bg abs"></section>
  <div class="overview-icon abs" role="img" aria-label="Small pencil and ruler icon"></div>
  <div class="overview">
    <h2 class="section-title abs">Agency Overview</h2>
    <p class="abs">Praesent varius faucibus nibh, nec imperdiet metus semper id. sent laoreet, leo quis gravida pretiuunc ipsum accumsan mi, sit ametique arcu massa sed mi. Semper dolor. Nullam tincidunt posuere laoreet. Cras et gravida nunc. Duis pharetra porttitor neque, tristique venenatis elit viverra rhoncus. Mauris tincidunt porta suscipit. <a>Read more...</a></p>
  </div>

  <div class="band abs" style="top:528px;height:30px"></div>

  <section class="products abs"></section>
  <article class="product" style="left:28px">
    <h3>Auto Insurance</h3>
    <div class="thumb"><span role="img" aria-label="Auto insurance illustration" style="background:linear-gradient(135deg,#dfe2f6,#8f95c8)"></span></div>
    <p>Auto Insurance covers you if your car is damaged or stolen, or if you cause an accident that injures others or their property. Let us help you select the coverage right for you.</p>
  </article>
  <article class="product" style="left:228px">
    <h3>Home Insurance</h3>
    <div class="thumb"><span role="img" aria-label="Home insurance illustration" style="background:linear-gradient(135deg,#f6e7a8,#b9b9b9)"></span></div>
    <p>Home Insurance covers your house and everything in it if it is damaged by fire, storm, theft or other disasters, plus liability for guests. Let us help you select the coverage right for you.</p>
  </article>
  <article class="product" style="left:442px">
    <h3>Auto &amp; Home Bundles</h3>
    <div class="thumb"><span role="img" aria-label="Bundled policies illustration" style="background:linear-gradient(135deg,#f9b48a,#f06a25)"></span></div>
    <p>Bundling your auto and home policies with one trusted agent saves money, simplifies billing and gives you one number to call when it matters. Let us help you select the coverage right for you.</p>
  </article>
  <article class="product" style="left:658px">
    <h3>Renters Coverage</h3>
    <div class="thumb"><span role="img" aria-label="Renters coverage illustration" style="background:linear-gradient(135deg,#fbe08a,#f5b820)"></span></div>
    <p>Renters Coverage protects your furniture, electronics and clothing when you rent, and covers liability if someone is hurt in your home. Let us help you select the coverage right for you.</p>
  </article>

  <section class="news-bg abs"></section>
  <div class="news">
    <h2 class="abs">Latest News &amp; Events</h2>
    <div class="arrow abs" style="left:760px"><svg width="8" height="10" viewBox="0 0 8 10"><path d="M6 1 2 5l4 4" stroke="#1b2f6b" stroke-width="2.5" fill="none"/></svg></div>
    <div class="arrow abs" style="left:790px"><svg width="8" height="10" viewBox="0 0 8 10"><path d="M2 1l4 4-4 4" stroke="#1b2f6b" stroke-width="2.5" fill="none"/></svg></div>
    <div class="news-photo abs" role="img" aria-label="Photo of business people in a meeting"></div>
    <h3 class="abs">Heading 1</h3>
    <p class="abs">Praesent varius faucibus nibh, nec imperdiet metus semper id. sent laoreet, leo quis gravida pretiuunc ipsum accumsan ami, sit ametique arcu massa sed mi. Semper dolor. sit ametique arcu massa sed mi. Semper dolor.</p>
    <div class="read abs">Read More...</div>
  </div>

  <footer class="site-footer abs"></footer>
  <h2 class="footer-title abs" style="left:31px">Agent Contact Information</h2>
  <div class="footer-text abs" style="left:30px;top:1019px">Address Line 1<br>Address Line 2<br>Phone no. : +1 555 0134 7720<br>Email :</div>
  <div class="btn abs" style="left:231px;top:1111px">READ MORE</div>

  <h2 class="footer-title abs" style="left:336px">Testimonial</h2>
  <div class="footer-text abs" style="left:336px;top:1013px;width:270px">Lorem ipsum dolor sit ipsum Lorem ipsum dolor sit ipsumLorem ipsum dolor sit ipsum</div>
  <div class="abs" style="left:336px;top:1053px;width:236px;border-top:1px dashed #888"></div>
  <div class="footer-text abs" style="left:336px;top:1061px;width:270px">Lorem ipsum dolor sit ipsum Lorem ipsum dolor sit ipsumLorem ipsum dolor sit ipsum</div>
  <div class="btn abs" style="left:564px;top:1111px">READ MORE</div>

  <h2 class="footer-title abs" style="left:658px">Get Social with Us</h2>
  <ul class="social abs">
    <li><i style="background:#3b5998"></i>Like me on Friendwall</li>
    <li><i style="background:#3fa9e0"></i>Follow me on Chirper</li>
    <li><i style="background:#e6e6e6"></i>Get in touch by Mail</li>
    <li><i style="background:#1b7dbb"></i>My Careerlink profile</li>
  </ul>

  <div class="footer-rule abs"></div>
  <div class="copyright abs">© 2012Company Name |  All Rights Reserved</div>
  <nav class="footer-nav">
    <a style="left:418px">Auto Insurance</a>
    <a style="left:514px">Home Insurance</a>
    <a style="left:614px">Products</a>
    <a style="left:682px">News</a>
    <a style="left:734px">Contact Us</a>
  </nav>
</div>
</body>
</html>
```